NLC Rio Verde Norte Artist Corinna Whitlatch event

Corinna Whitlatch

Elevate your appreciation for the arts with an Only-in-NLC VIP tour of the priceless art collection of El Paso's mysterious Corinna, including access to her museum which is not open to the public. Dinner and transportation between sites included.

Corinna Whitlatch lives and works in El Paso, Texas. Praised by the Harbor Ledger Daily as "fresh," "a tough act to follow," and the "ultimate in transgression," Whitlatch is widely recognized in her home state of Texas as a unique presence and highly original artist. She has been characterized by Delia Frank, former curator at the Bayridge Gallery of Fine Work, as "an anachronism who earnestly pursues a long-held tradition of landscape and genre painting . . . inspired by her Southwestern environment and vivid imagination.

Rendered with thick applications of radiant colors, Whitlatch's paintings are intensely personal, dream-like explorations of the natural world.
DATE: Wednesday, September 26, 2018
VENUE: RIVERBEND CIVIC TRUST HALL
718 W Tamsin Ave
El Paso, TX 79948
United States
AGENDA: 6:00 - 7:30 Light supper and orientation to the mysterious Corinna Whitlatch, Riverbend Civic Trust Hall downtown
7:30 - 7:45 Board van to go to Sunward Health Campus Corinna Whitlatch Chapel
7:45 - 8:15 View Chapel
8:15 - 8:30 Board van to go to Museum Whitlatch
8:30 - 9:15 View Museum Whitlatch with dessert
9:15 - 9:30 Return downtown
RESOURCE(S): Tessa Brund - Being an icon in the art world, and not needing any introduction, Tessa probably knows more about Corinna Whitlatch than anyone!

Wade Hollins – President and CEO of the Riverbend Civic Trust since 2011

Lorinda Vasko - Director of Presentations of the Corinna Whitlatch Museum and an art history graduate of GSVC

Owen Strade - Nobody has ever actually seen Corinna Whitlatch, yet ophthalmologist and NLC member Dr. Owen Strade is her eye surgeon. How can that be? Find out at the event!
ATTENDANCE: NLC Members, NLC Spouses/Guests, NLC SAGE Members, NLC SAGE Spouses/Guests
ATTIRE: Business Casual
DAY CHAIRS: Owen Strade
Tessa Brund

Invite 5x7 or 7x5 please

Target Market(s)

NLC Rio Verde Norte Members

Industry/Entity Type

Non Profit

Font styles to use
Decorative
Script

Colors

Designer to choose colors to be used in the design.

Requirements
Must have
• Event title
• Date
• Artist description (Corinna Whitlatch)
• Venue
• Attire
• Attendees
• Logos
Nice to have
• Information about the artist
Should not have
• Art from another artists

```html
<!DOCTYPE html>
<html lang="en">
<head>
<meta charset="utf-8">
<title>Corinna Whitlatch – NLC Rio Verde Norte Invitation</title>
<link rel="stylesheet" href="https://fonts.googleapis.com/css2?family=Roboto:wght@400;500;700&family=Great+Vibes&display=swap">
<style>
  :root {
    --stage: #9b9797;
    --paper: #ffffff;
    --ink: #3a3a3a;
    --ink-soft: #4a4a4a;
    --marigold: #f8ad1a;
    --marigold-deep: #f39a12;
    --line-light: #fff4dc;
  }
  * { margin: 0; padding: 0; box-sizing: border-box; }
  html, body { width: 1200px; height: 753px; overflow: hidden; background: var(--stage); }
  body { position: relative; font-family: "Roboto", Arial, sans-serif; color: var(--ink); }

  .page { position: absolute; top: 0; height: 753px; width: 538px; background: var(--paper); overflow: hidden; }
  .page--front { left: 46px; }
  .page--back { left: 608px; }

  /* Front */
  .artwork-band {
    position: absolute; left: 0; top: 0; width: 538px; height: 310px;
    background:
      radial-gradient(ellipse at 20% 20%, #f7b52c 0%, rgba(247,181,44,0) 55%),
      radial-gradient(ellipse at 85% 55%, #d9557a 0%, rgba(217,85,122,0) 45%),
      radial-gradient(ellipse at 70% 90%, #5f88c9 0%, rgba(95,136,201,0) 45%),
      radial-gradient(ellipse at 40% 70%, #f5e26a 0%, rgba(245,226,106,0) 55%),
      linear-gradient(135deg, #fbd36b, #f6a63a 50%, #e8b6c8);
  }
  .artist-bio {
    position: absolute; left: 53px; top: 74px; width: 431px;
    column-count: 2; column-gap: 26px;
    font-size: 11.2px; line-height: 16px; text-align: justify; color: var(--ink);
  }
  .artist-bio p { margin: 0; }
  .drop-cap {
    float: left; font-size: 72px; line-height: 56px; font-weight: 400;
    margin: 3px 4px 0 0; color: var(--ink);
  }
  .event-title {
    position: absolute; left: 78px; top: 326px; width: 400px;
    font-family: "Great Vibes", cursive; font-weight: 400;
    font-size: 86px; line-height: 82px; color: var(--ink);
  }
  .event-title .line2 { display: block; padding-left: 0; }
  .event-title .line1 { display: block; padding-left: 50px; }
  .tagline {
    position: absolute; left: 72px; top: 522px; width: 381px;
    font-size: 13.6px; line-height: 21px; font-weight: 500; text-align: justify; color: var(--ink);
  }
  .tagline strong { font-weight: 700; }
  .event-details { position: absolute; left: 76px; top: 658px; font-size: 8.8px; line-height: 13.6px; color: var(--ink); }
  .event-details b { font-weight: 700; }

  /* Back */
  .color-field {
    position: absolute; left: 0; top: 0; width: 538px; height: 524px;
    background:
      radial-gradient(ellipse at 80% 100%, #f59a10 0%, rgba(245,154,16,0) 45%),
      radial-gradient(ellipse at 15% 95%, #f7a418 0%, rgba(247,164,24,0) 40%),
      linear-gradient(180deg, var(--marigold) 0%, var(--marigold) 80%, var(--marigold-deep) 100%);
  }
  .section-heading { font-size: 17.6px; font-weight: 700; color: var(--ink); letter-spacing: 0.2px; }
  .resources { position: absolute; left: 54px; top: 73px; width: 440px; }
  .resources .cols { display: flex; margin-top: 0; }
  .resources .col { font-size: 12px; line-height: 16px; color: var(--ink); }
  .resources .col--a { width: 206px; padding-right: 8px; border-right: 1px solid var(--line-light); }
  .resources .col--b { width: 234px; padding-left: 20px; }
  .resources p + p { margin-top: 16px; }
  .resources b { font-weight: 700; }

  .agenda {
    position: absolute; left: 54px; top: 290px; width: 430px; height: 192px;
    border: 1.6px solid var(--paper); padding: 9px 14px 0;
  }
  .agenda .cols { display: flex; }
  .agenda .col { font-size: 12px; line-height: 16px; color: var(--ink); }
  .agenda .col--a { width: 193px; padding-right: 8px; border-right: 1px solid var(--line-light); height: 144px; }
  .agenda .col--b { padding-left: 14px; }
  .agenda p + p { margin-top: 16px; }
  .agenda b { font-weight: 700; }

  .brand-row { position: absolute; left: 0; top: 556px; width: 538px; display: flex; justify-content: center; gap: 34px; align-items: flex-end; }
  .brand { text-align: center; color: var(--ink); font-family: "Roboto", Arial, sans-serif; font-weight: 500; }
  .brand__mark { display: block; width: 20px; height: 20px; background: var(--ink); margin: 0 auto 8px; }
  .brand__name { font-size: 22px; letter-spacing: 2px; line-height: 24px; }
  .brand__sub { font-size: 8px; letter-spacing: 1px; line-height: 12px; }
  .venue-info { position: absolute; left: 0; top: 652px; width: 538px; text-align: center; font-size: 12px; line-height: 16px; color: var(--ink); }
  .venue-info b { font-weight: 700; }
  .footer-bar { position: absolute; left: 118px; top: 744px; width: 300px; height: 9px; background: var(--marigold); }
</style>
</head>
<body>
  <section class="page page--front">
    <div class="artwork-band" role="img" aria-label="Watercolor wash in golden yellow, rose and blue"></div>
    <div class="artist-bio">
      <p><span class="drop-cap">A</span>Corinna Whitlatch lives and works in El Paso, Texas. Praised by the Harbor Ledger Daily as “fresh,” “a tough act to follow,” and the “ultimate in transgression,” Whitlatch is widely recognized in her home state of Texas as a unique presence and highly original artist. She has been characterized by Delia Frank, former curator at the Bayridge Gallery of Fine Work, as “an anachronism who earnestly pursues a long-held tradition of landscape and genre painting . . . inspired by her Southwestern environment and vivid imagination.</p>
      <p>Rendered with thick applications of radiant colors, Whitlatch’s paintings are intensely personal, dream-like explorations of the natural world.</p>
    </div>
    <h1 class="event-title"><span class="line1">Corinna</span><span class="line2">Whitlatch</span></h1>
    <p class="tagline">Elevate your appreciation for the arts with an Only-in-NLC VIP tour of the <strong>PRICELESS ART COLLECTION</strong> of <strong>EL PASO’S MYSTERIOUS CORINNA,</strong> including access to her museum which is not open to the public. Dinner and transportation between sites included.</p>
    <div class="event-details">
      <p><b>ATTENDEES:</b> NLC Member/Spouse, NLC SAGE Member/Spouse</p>
      <p><b>ATTIRE:</b> Business Casual</p>
      <p><b>DAY CHAIRS:</b> Owen Strade, Tessa Brund</p>
    </div>
  </section>

  <section class="page page--back">
    <div class="color-field"></div>
    <div class="resources">
      <h2 class="section-heading">RESOURCE(S):</h2>
      <div class="cols">
        <div class="col col--a">
          <p><b>Tessa Brund</b> – Being an icon in the art world, and not needing any introduction, Tessa probably knows more about Corinna Whitlatch than anyone!</p>
          <p><b>Wade Hollins</b> – President and CEO of the Riverbend Civic Trust since 2011</p>
        </div>
        <div class="col col--b">
          <p><b>Lorinda Vasko</b> – Director of Presentations of the Corinna Whitlatch Museum and an art history graduate of GSVC</p>
          <p><b>Owen Strade</b> – Nobody has ever actually seen Corinna Whitlatch, yet ophthalmologist and NLC member Dr. Owen Strade is her eye surgeon. How can that be? Find out at the event!</p>
        </div>
      </div>
    </div>

    <div class="agenda">
      <h2 class="section-heading">AGENDA:</h2>
      <div class="cols">
        <div class="col col--a">
          <p><b>6:00 - 7:30</b> Light supper and orientation to the mysterious Corinna Whitlatch, Riverbend Civic Trust Hall downtown</p>
          <p><b>7:30 - 7:45</b> Board van to go to Sunward Health Campus Corinna Whitlatch Chapel</p>
        </div>
        <div class="col col--b">
          <p><b>7:45 - 8:15</b> View Chapel</p>
          <p><b>8:15 - 8:30</b> Board van to go to Museum Whitlatch</p>
          <p><b>8:30 - 9:15</b> View Museum Whitlatch with dessert</p>
          <p><b>9:15 - 9:30</b> Return downtown</p>
        </div>
      </div>
    </div>

    <div class="brand-row">
      <div class="brand">
        <span class="brand__mark"></span>
        <div class="brand__name">ASCEND 915</div>
        <div class="brand__sub">RIO VERDE NORTE 2018/2019</div>
      </div>
      <div class="brand">
        <span class="brand__mark"></span>
        <div class="brand__name">NLC</div>
        <div class="brand__sub">Rio Verde Norte Chapter</div>
      </div>
    </div>

    <div class="venue-info">
      <p><b>DATE:</b> Wednesday, September 26, 2018</p>
      <p><b>VENUE:</b> RIVERBEND CIVIC TRUST HALL</p>
      <p>718 W Tamsin Ave</p>
      <p>El Paso, TX 79948</p>
      <p>United States</p>
    </div>
    <div class="footer-bar"></div>
  </section>
</body>
</html>
```